Boutique Sparkling Blanc de Blancs Wine label

We are looking for a label and neck label for our new Sparkling Chardonnay.
Images uploaded include, bubbles and glitter maybe as a faded background for whole label?
We like Refined, elegant yet simple designs.
Have included our current table chardonnay label as example.

Industry/Entity Type

Boutique

Font styles to use
Decorative
Script

Requirements
Must have
• Name - "Every Moonlit Hour"
• Methode Traditionelle
• Blanc de Blancs
• 2015
• Beyond the Orchards (Brand)
• Adelaide Hills
Nice to have
• Neutral tones
• Sparkles, Glitter, Bubbles
• Traditional, cursive or vine like fonts
• Have attached fonts we used for previous wine label - might be nice to carry through same/similar fonts to continue our brand?
Should not have
• a lot of colour

```html
<!DOCTYPE html>
<html lang="en">
<head>
<meta charset="utf-8">
<title>Every Moonlit Hour – Sparkling Blanc de Blancs Label</title>
<link rel="stylesheet" href="https://fonts.googleapis.com/css2?family=Pinyon+Script&display=swap">
<style>
  :root {
    --page: #ffffff;
    --glitter-light: #fbf6c8;
    --glitter-mid: #efe49a;
    --glitter-deep: #e2d27a;
    --ink: #c2b62a;
    --ink-dark: #8f8512;
    --emboss-light: rgba(255, 255, 240, 0.9);
    --vine: #d9d2a6;
  }
  html, body {
    margin: 0;
    padding: 0;
    width: 1200px;
    height: 1184px;
    overflow: hidden;
    background: var(--page);
  }
  .canvas {
    position: relative;
    width: 1200px;
    height: 1184px;
  }
  .label {
    position: absolute;
    left: 40px;
    top: 12px;
    width: 1120px;
    height: 1160px;
    overflow: hidden;
  }
  .label__glitter {
    position: absolute;
    inset: 0;
    background:
      radial-gradient(ellipse at 30% 10%, var(--glitter-light) 0%, transparent 55%),
      radial-gradient(ellipse at 80% 90%, var(--glitter-light) 0%, transparent 50%),
      linear-gradient(180deg, var(--glitter-light) 0%, var(--glitter-mid) 45%, var(--glitter-deep) 70%, var(--glitter-mid) 100%);
  }
  .label__vine {
    position: absolute;
    left: 102px;
    width: 940px;
    height: 140px;
    background: radial-gradient(ellipse at center, var(--vine) 0%, rgba(217, 210, 166, 0.35) 55%, transparent 75%);
  }
  .label__vine--top { top: 52px; }
  .label__vine--bottom { top: 956px; }
  .label__text {
    position: absolute;
    left: 0;
    right: 0;
    margin: 0;
    text-align: center;
    font-family: "Pinyon Script", cursive;
    font-weight: 400;
    color: var(--ink);
    letter-spacing: 0.12em;
    line-height: 1;
    text-shadow: -1px -1px 0 var(--emboss-light), 2px 2px 2px var(--ink-dark);
    white-space: nowrap;
  }
  .label__name { top: 250px; font-size: 104px; }
  .label__method { top: 400px; font-size: 66px; }
  .label__style { top: 500px; font-size: 66px; }
  .label__vintage { top: 608px; font-size: 86px; letter-spacing: 0.08em; }
  .label__estate { top: 728px; font-size: 66px; }
  .label__region { top: 828px; font-size: 66px; }
</style>
</head>
<body>
<main class="canvas">
  <section class="label" aria-label="Sparkling wine label">
    <div class="label__glitter" role="img" aria-label="Soft pale gold glitter and bokeh background"></div>
    <div class="label__vine label__vine--top" role="img" aria-label="Embossed grapevine ornament with grape clusters and leaves"></div>
    <h1 class="label__text label__name">Every Moonlit Hour</h1>
    <p class="label__text label__method">Methode Traditionelle</p>
    <p class="label__text label__style">Blanc de Blancs</p>
    <p class="label__text label__vintage">2015</p>
    <p class="label__text label__estate">Beyond the Orchards</p>
    <p class="label__text label__region">Adelaide Hills</p>
    <div class="label__vine label__vine--bottom" role="img" aria-label="Embossed grapevine ornament with grape clusters and leaves"></div>
  </section>
</main>
</body>
</html>
```